Consulting & Education Company Needs Dynamic MS Word Template

We need a MS Word Template for everyday documents. This would be leveraged to create reports, marketing materials, internal memos etc.

The document should follow the standard MS Word template format and have an H1,H2,H3, paragraph, Title, bold font, regular font, table etc. All editable with normal MS Word features.

Attached is a Logo which was created by one of the many talented folks here at ArtHarbor. We would like to see the same color scheme used throughout the document. Additional attached is a sample word document that outlines all of the components we would like to see in the template.

Target Market(s)

Information Security - Penetration Testing - IT - Network/Systems Engineering

Industry/Entity Type

Education

Requirements
Must have
• Submission must meet all standard MS Word Template requirements.
• Submission should make use of Built in MS Styles so as the user of the template I shoudl be able to create a brand new page and insert an H1 for example and be able to select from the styles drop down the same font/color/style that you have designed for your submission.
• All sections in the provided document need to be contained in your submission.
• The table of contents should auto update if I add a new page, heading, section etc.
• Need to read and understand all of my comments which I have placed in the sample document uploaded to the briefing
Nice to have
• the cover page should be eye catching but not over the top. Some cool vectors/bg colors etc that look nice with the logo already provided.
• Icons and vectors whever they make sense and are visually appealing. For example the document has a section for defiing severity risk: Critical, High, Medium and Low it would be great if there was a nice icon or 2d graphic associated with each one. also color coded is a plus High is more dangerous then medium so the colors should communicate that.
Should not have
• no fixed textboxes or image boxes. everything needs to be smoothly editable in MS Word. "Editable" means more than just being able to alter text.

```html
<!DOCTYPE html>
<html lang="en">
<head>
<meta charset="utf-8">
<title>ProbeWise – Report Template Pages</title>
<link rel="stylesheet" href="https://fonts.googleapis.com/css2?family=Roboto+Condensed:wght@300;400;700&family=Roboto:wght@400;700&display=swap">
<style>
:root{
  --canvas:#f5f5f5;
  --band:#e4e4e4;
  --paper:#ffffff;
  --red:#d71920;
  --red-dark:#a50f14;
  --pink:#f6c4c6;
  --ink:#2a2a2a;
  --muted:#6d6d6d;
  --rule:#cfcfcf;
  --black:#111111;
  --crit:#c8102e;
  --high:#e8401c;
  --med:#f7b500;
  --low:#8dc63f;
  --head:"Roboto Condensed",Arial,sans-serif;
  --text:"Roboto",Arial,sans-serif;
}
*{box-sizing:border-box;margin:0;padding:0}
html,body{width:696px;height:1200px;overflow:hidden;background:var(--canvas)}
body{position:relative;font-family:var(--text);color:var(--ink)}
.row-band{position:absolute;left:8px;width:680px;height:292px;background:var(--band)}
.page{position:absolute;width:212px;height:280px;background:var(--paper);overflow:hidden;box-shadow:0 0 2px rgba(0,0,0,.12)}
.page-tab{position:absolute;left:8px;top:0;width:96px;height:9px;background:var(--red);clip-path:polygon(0 0,100% 0,93% 100%,0 100%)}
.page-tab::after{content:"";position:absolute;left:0;top:0;width:100%;height:100%}
.brand{position:absolute;right:9px;top:8px;display:flex;align-items:center;gap:2px;font-family:var(--head);font-weight:700;font-size:6px;letter-spacing:.2px;color:var(--red);text-transform:uppercase}
.brand-square{width:5px;height:5px;background:var(--red)}
.page-foot{position:absolute;right:0;bottom:0;width:40px;height:8px;background:var(--red);clip-path:polygon(12% 0,100% 0,100% 100%,0 100%);color:#fff;font-size:3.5px;display:flex;align-items:center;justify-content:flex-end;padding-right:6px}
.page-body{position:absolute;left:20px;right:20px;top:30px}
h1{font-family:var(--head);font-weight:400;font-size:10.5px;color:var(--ink);margin-bottom:4px}
h2{font-family:var(--head);font-weight:400;font-size:7.5px;color:var(--ink);margin:6px 0 3px}
p{font-size:3.4px;line-height:1.45;color:var(--muted);text-align:justify}
.hex-field{position:absolute;right:0;bottom:0;width:70px;height:110px;background:linear-gradient(160deg,rgba(215,25,32,0) 20%,rgba(215,25,32,.07))}

/* cover */
.cover-brand{position:absolute;left:30px;top:40px;display:flex;align-items:center;gap:4px;font-family:var(--head);font-weight:700;font-size:13px;color:var(--red);text-transform:uppercase}
.cover-brand .brand-square{width:12px;height:12px}
.cover-client{position:absolute;left:30px;top:102px;font-family:var(--head);font-size:8px;color:var(--red);text-transform:uppercase}
.cover-title{position:absolute;left:30px;top:111px;font-family:var(--head);font-weight:300;font-size:16px;color:var(--ink);text-transform:uppercase}
.cover-date{position:absolute;left:31px;top:132px;font-size:4px;color:var(--muted)}
.cover-pattern{position:absolute;right:0;bottom:0;width:130px;height:140px;background:linear-gradient(135deg,rgba(215,25,32,0) 30%,rgba(215,25,32,.16))}

/* contents */
.toc{list-style:none;margin-top:10px}
.toc li{display:flex;font-size:3.2px;font-weight:700;color:var(--ink);margin-top:3px}
.toc li.sub{font-weight:400;color:var(--muted);margin-top:1px}
.toc li .dots{flex:1;border-bottom:.4px dotted var(--muted);margin:0 1px 1px}
.toc li.gap{margin-top:6px}

/* data tables */
.data-table{width:100%;border-collapse:collapse;margin:5px 0;font-size:3.2px;border:.5px solid var(--rule)}
.data-table caption{text-align:left;font-family:var(--head);font-size:6px;color:#fff;padding:3px 3px;caption-side:top}
.data-table th{font-weight:400;text-align:left;padding:2px 3px;color:#fff;font-size:3.6px}
.data-table td{padding:2px 3px;vertical-align:top;color:var(--ink)}
.data-table ul{padding-left:5px}
.table-red caption{background:var(--red)}
.table-red th{background:var(--pink)}
.table-black caption{background:var(--black)}
.table-black th{background:#a8a8a8}
.findings-table th{background:#8b8b8b;font-weight:700}
.findings-table th.sev,.findings-table td.sev{text-align:center;width:35%}
.findings-table td{border-top:.5px solid var(--rule)}
.sev-crit{color:var(--crit)} .sev-high{color:var(--high)} .sev-med{color:var(--med)} .sev-low{color:var(--low)}

/* severity chart */
.severity-chart{position:absolute;left:6px;right:6px;top:92px}
.severity-chart svg{display:block;width:200px;height:82px}
.severity-labels,.severity-notes{display:grid;grid-template-columns:repeat(4,1fr);gap:1px}
.severity-labels span{font-family:var(--head);font-size:4px;color:#fff;text-align:center;padding:3px 0}
.severity-notes div{font-size:3.1px;line-height:1.5;color:var(--muted);padding:4px 5px;height:70px}
.lbl-low{background:var(--low)} .lbl-med{background:var(--med)} .lbl-high{background:var(--high)} .lbl-crit{background:var(--crit)}
.note-low{background:#eef6e2} .note-med{background:#fff4d6} .note-high{background:#fde0d6} .note-crit{background:#f9d3d8}

/* detailed observations */
.finding-title{display:flex;align-items:center;gap:3px;font-family:var(--head);font-size:6px;margin:-1px 0 4px}
.finding-title .badge{width:9px;height:9px;border-radius:50%;background:var(--c2);display:flex;align-items:center;justify-content:center}
.finding-title span{color:var(--c2)}
.finding{width:100%;border:.5px solid #999;display:grid;grid-template-columns:23px 1fr}
.finding .side{color:#fff;font-size:2.8px;font-weight:700;display:flex;flex-direction:column;align-items:center;justify-content:center;gap:2px;text-align:center}
.finding .side svg{width:7px;height:7px}
.finding .cell{padding:2px 3px;font-size:2.8px;line-height:1.45;color:var(--ink);border-bottom:.5px solid var(--rule)}
.finding .side.hd{background:var(--black);height:15px}
.finding .cell.hd{background:var(--black);color:#fff;text-align:center;font-size:3.2px;display:flex;align-items:center;justify-content:center}
.finding .s1{background:var(--c1);height:36px}
.finding .s2{background:var(--c2);height:68px}
.finding .s3{background:var(--c3);height:30px}
.finding .s4{background:var(--c4);height:16px}
.evidence{width:70px;height:48px;margin:4px auto 2px;border:.5px solid #bbb;background:linear-gradient(180deg,#dfe6ef,#f4f6f8 40%,#e3e8ee)}
.finding .caption{font-size:2.4px;text-align:center;color:var(--muted)}
.finding ul{padding-left:6px;margin-top:1px}
.finding ul.plain{list-style:disc}
.crit{--c1:#e0585d;--c2:#c8102e;--c3:#9e0d24;--c4:#6b0a18}
.high{--c1:#f47a5a;--c2:#e8401c;--c3:#b8321a;--c4:#7a2010}
.med{--c1:#ffd54f;--c2:#f7b500;--c3:#b98a10;--c4:#7a5c0a}
.low{--c1:#b5dc7a;--c2:#8dc63f;--c3:#5e9a2a;--c4:#3d6a1a}

/* appendix & contact */
.appendix-title{color:var(--red-dark)}
.appendix-sub{color:var(--red);font-size:6px;margin-top:0}
.contact-photo{width:172px;height:90px;margin-top:4px;background:linear-gradient(180deg,#e8e8e8,#c9c9c9 60%,#a9a9a9)}
.contact-list{list-style:none;margin-top:10px}
.contact-list li{display:grid;grid-template-columns:9px 1fr;column-gap:3px;margin-bottom:4px;font-size:3.2px;color:var(--muted)}
.contact-list .icon{grid-row:span 2;width:7px;height:7px;border-radius:50%;background:var(--red);display:flex;align-items:center;justify-content:center}
.contact-list .icon svg{width:4px;height:4px}
.contact-list strong{font-weight:400;color:var(--red);font-size:3.6px}
</style>
</head>
<body>

<div class="row-band" style="top:8px"></div>
<div class="row-band" style="top:306px"></div>
<div class="row-band" style="top:604px"></div>
<div class="row-band" style="top:902px"></div>

<!-- Cover -->
<section class="page" style="left:18px;top:14px">
  <div class="cover-brand"><span class="brand-square"></span>ProbeWise</div>
  <div class="cover-client">Client Name</div>
  <div class="cover-title">Engagement Title</div>
  <div class="cover-date">Month Day, Year</div>
  <div class="cover-pattern" role="img" aria-label="Cluster of outlined red hexagons rising from the lower right corner"></div>
</section>

<!-- Contents -->
<section class="page" style="left:242px;top:14px">
  <div class="page-tab"></div>
  <div class="brand"><span class="brand-square"></span>ProbeWise</div>
  <div class="page-body">
    <h1>Contents</h1>
    <ul class="toc">
      <li>ENGAGEMENT OVERVIEW<span class="dots"></span>1</li>
      <li>Engagement Scope<span class="dots"></span>1</li>
      <li>Engagement Summary<span class="dots"></span>1</li>
      <li>Key Observations<span class="dots"></span>1</li>
      <li class="gap">TECHNICAL OVERVIEW<span class="dots"></span>1</li>
      <li>Severity Ratings<span class="dots"></span>1</li>
      <li>Summary Of Findings<span class="dots"></span>1</li>
      <li class="gap">Detailed Observations<span class="dots"></span>1</li>
      <li class="sub">Critical Findings<span class="dots"></span>1</li>
      <li>Detailed Observations<span class="dots"></span>1</li>
      <li class="sub">High Findings<span class="dots"></span>1</li>
      <li>Detailed Observations<span class="dots"></span>1</li>
      <li class="sub">Medium Findings<span class="dots"></span>1</li>
      <li>Detailed Observations<span class="dots"></span>1</li>
      <li class="sub">Low Findings<span class="dots"></span>1</li>
      <li class="gap">APPENDIX 01<span class="dots"></span>1</li>
      <li class="sub">Engagement Methodology<span class="dots"></span>1</li>
      <li class="gap">OUR CONTACT<span class="dots"></span>1</li>
    </ul>
  </div>
  <div class="hex-field" role="img" aria-label="Faint hexagon pattern"></div>
  <div class="page-foot">1</div>
</section>

<!-- Engagement overview -->
<section class="page" style="left:466px;top:14px">
  <div class="page-tab"></div>
  <div class="brand"><span class="brand-square"></span>ProbeWise</div>
  <div class="page-body">
    <h1>Engagement Overview</h1>
    <p>This report sets out the goals, timing and boundaries of the assessment carried out for the client. It explains who took part, which systems were in view and how the team shared progress with staff during each stage of the work.</p>
    <h2>Engagement Scope</h2>
    <p>The scope covered the listed hosts and web applications. Any system outside these ranges was not tested unless written approval was given first.</p>
    <table class="data-table table-red">
      <caption>TABLE ONE</caption>
      <tr><th>Sub heading 2</th><th>Sub heading 2</th></tr>
      <tr><td><ul><li>Target 1</li><li>Target 2</li></ul></td><td><ul><li>Target 3</li><li>Target 4</li></ul></td></tr>
    </table>
    <h2>Engagement Summary</h2>
    <p>Testing found several weak points in configuration, patching and access control. Most issues can be fixed quickly with settings changes and routine updates. A few require design review. Each finding below lists the risk, the evidence gathered and clear steps to close the gap, so teams can plan fixes in order of impact and effort across the coming quarter.</p>
  </div>
  <div class="hex-field" role="img" aria-label="Faint hexagon pattern"></div>
  <div class="page-foot">2</div>
</section>

<!-- Key observations -->
<section class="page" style="left:18px;top:312px">
  <div class="page-tab"></div>
  <div class="brand"><span class="brand-square"></span>ProbeWise</div>
  <div class="page-body">
    <h1>Key Observations</h1>
    <p>The points below summarise the most important patterns seen across the environment. They give leaders a quick view of overall posture before the technical detail that follows in later sections of this report.</p>
    <table class="data-table table-black">
      <caption>TABLE TWO</caption>
      <tr><th>Sub heading 2</th><th>Sub heading 2</th></tr>
      <tr><td><ul><li>Target 1</li><li>Target 2</li></ul></td><td><ul><li>Target 3</li><li>Target 4</li></ul></td></tr>
    </table>
  </div>
  <div class="hex-field" role="img" aria-label="Faint hexagon pattern"></div>
  <div class="page-foot">3</div>
</section>

<!-- Technical overview -->
<section class="page" style="left:242px;top:312px">
  <div class="page-tab"></div>
  <div class="brand"><span class="brand-square"></span>ProbeWise</div>
  <div class="page-body">
    <h1>Technical Overview</h1>
    <p>This section describes the tools and methods used and how each issue was rated. Ratings weigh likely impact against ease of attack to rank the work.</p>
    <h2>Severity Ratings</h2>
  </div>
  <div class="severity-chart">
    <svg viewBox="0 0 200 82" aria-label="Severity levels one to four rising in height">
      <g font-family="Roboto Condensed, Arial, sans-serif" font-weight="700" font-size="10" text-anchor="middle">
        <polygon points="6,56 25,48 44,56 44,82 6,82" fill="#8dc63f"/>
        <circle cx="25" cy="66" r="6" fill="#fff"/>
        <text x="25" y="44" fill="#2bb3c0">1</text>
        <polygon points="56,46 75,38 94,46 94,82 56,82" fill="#f7b500"/>
        <circle cx="75" cy="56" r="6" fill="#fff"/>
        <text x="75" y="34" fill="#f7b500">2</text>
        <polygon points="106,34 125,26 144,34 144,82 106,82" fill="#e8401c"/>
        <circle cx="125" cy="44" r="6" fill="#fff"/>
        <text x="125" y="22" fill="#e8401c">3</text>
        <polygon points="156,22 175,14 194,22 194,82 156,82" fill="#c8102e"/>
        <circle cx="175" cy="32" r="6" fill="#fff"/>
        <text x="175" y="10" fill="#c8102e">4</text>
        <g fill="#888">
          <rect x="22" y="66" width="1.5" height="3"/><rect x="24.5" y="64" width="1.5" height="5"/><rect x="27" y="62" width="1.5" height="7"/>
          <rect x="72" y="56" width="1.5" height="3"/><rect x="74.5" y="54" width="1.5" height="5"/><rect x="77" y="52" width="1.5" height="7"/>
          <rect x="122" y="44" width="1.5" height="3"/><rect x="124.5" y="42" width="1.5" height="5"/><rect x="127" y="40" width="1.5" height="7"/>
          <rect x="172" y="32" width="1.5" height="3"/><rect x="174.5" y="30" width="1.5" height="5"/><rect x="177" y="28" width="1.5" height="7"/>
        </g>
      </g>
    </svg>
    <div class="severity-labels">
      <span class="lbl-low">LOW</span><span class="lbl-med">MEDIUM</span><span class="lbl-high">HIGH</span><span class="lbl-crit">CRITICAL</span>
    </div>
    <div class="severity-notes">
      <div class="note-low">Minor issue with little direct impact. Fix during normal upkeep when time allows and track for any change in exposure.</div>
      <div class="note-med">Moderate issue that may help an attacker when combined with others. Plan a fix within the next release cycle.</div>
      <div class="note-high">Serious flaw that can expose data or systems. Fix soon and add monitoring until the change is fully in place.</div>
      <div class="note-crit">Severe flaw open to easy attack with major impact. Act at once and confirm the fix through retesting.</div>
    </div>
  </div>
  <div class="page-foot">4</div>
</section>

<!-- Summary of findings -->
<section class="page" style="left:466px;top:312px">
  <div class="page-tab"></div>
  <div class="brand"><span class="brand-square"></span>ProbeWise</div>
  <div class="page-body">
    <h1>Summary Of Findings</h1>
    <p>The table lists each finding with its rating. Full detail for every item appears in the observation pages that follow this summary.</p>
    <table class="data-table table-red findings-table">
      <caption>Table 3</caption>
      <tr><th>Finding Name</th><th class="sev">Severity</th></tr>
      <tr><td>Critical Finding Title</td><td class="sev sev-crit">Critical</td></tr>
      <tr><td>High Finding Title</td><td class="sev sev-high">High</td></tr>
      <tr><td>Medium Finding Title</td><td class="sev sev-med">Medium</td></tr>
      <tr><td>Low Finding Title</td><td class="sev sev-low">Low</td></tr>
    </table>
  </div>
  <div class="hex-field" role="img" aria-label="Faint hexagon pattern"></div>
  <div class="page-foot">5</div>
</section>

<!-- Detailed: critical -->
<section class="page crit" style="left:18px;top:610px">
  <div class="page-tab"></div>
  <div class="brand"><span class="brand-square"></span>ProbeWise</div>
  <div class="page-body">
    <h1>Detailed Observations</h1>
    <div class="finding-title"><div class="badge"><svg width="5" height="5" viewBox="0 0 5 5" fill="#fff"><rect x="0" y="3" width="1" height="2"/><rect x="2" y="2" width="1" height="3"/><rect x="4" y="0" width="1" height="5"/></svg></div><span>Critical Findings</span></div>
    <div class="finding">
      <div class="side hd">Insecure Configurations Identified</div><div class="cell hd">Critical</div>
      <div class="side s1"><svg viewBox="0 0 10 10" fill="none" stroke="#fff" stroke-width="1.4"><circle cx="4" cy="4" r="3"/><path d="M6.2 6.2 9 9"/></svg>Observation</div>
      <div class="cell">The public web server exposes default admin pages and verbose banners. These reveal software versions and let any remote visitor reach login forms that still accept factory passwords, giving full control of the host.</div>
      <div class="side s2"><svg viewBox="0 0 10 10" fill="none" stroke="#fff" stroke-width="1.2"><rect x="1" y="3" width="8" height="6"/><path d="M3.5 3V1.5h3V3"/></svg>Evidence</div>
      <div class="cell"><div class="evidence" role="img" aria-label="Screenshot of the exposed admin console"></div><div class="caption">Figure #1 – This is a caption for the above screenshot</div></div>
      <div class="side s3"><svg viewBox="0 0 10 10" fill="none" stroke="#fff" stroke-width="1.2"><rect x="2" y="1.5" width="6" height="8"/><path d="M4 4h2M4 6h2"/></svg>Recommendation</div>
      <div class="cell"><b>Remove</b> default pages, change all stock passwords and hide version banners on every exposed service.<ul><li>Limit admin access to the internal network only.</li><li>Review settings after each update or new deployment.</li></ul></div>
      <div class="side s4"><svg viewBox="0 0 10 10" fill="none" stroke="#fff" stroke-width="1.2"><rect x="1" y="1.5" width="8" height="5.5"/><path d="M5 7v2M3 9h4"/></svg>Assets Affected</div>
      <div class="cell"><ul><li>127.0.0.1</li><li>127.0.0.2</li><li>127.0.0.3</li></ul></div>
    </div>
  </div>
  <div class="page-foot">6</div>
</section>

<!-- Detailed: high -->
<section class="page high" style="left:242px;top:610px">
  <div class="page-tab"></div>
  <div class="brand"><span class="brand-square"></span>ProbeWise</div>
  <div class="page-body">
    <h1>Detailed Observations</h1>
    <div class="finding-title"><div class="badge"><svg width="5" height="5" viewBox="0 0 5 5" fill="#fff"><rect x="0" y="3" width="1" height="2"/><rect x="2" y="2" width="1" height="3"/><rect x="4" y="0" width="1" height="5"/></svg></div><span>High Findings</span></div>
    <div class="finding">
      <div class="side hd">Insecure Configurations Identified</div><div class="cell hd">Critical</div>
      <div class="side s1"><svg viewBox="0 0 10 10" fill="none" stroke="#fff" stroke-width="1.4"><circle cx="4" cy="4" r="3"/><path d="M6.2 6.2 9 9"/></svg>Observation</div>
      <div class="cell">File shares on the office network allow read access to all staff accounts. Several folders hold backups and scripts that contain stored service credentials in plain text, which could be reused against other systems.</div>
      <div class="side s2"><svg viewBox="0 0 10 10" fill="none" stroke="#fff" stroke-width="1.2"><rect x="1" y="3" width="8" height="6"/><path d="M3.5 3V1.5h3V3"/></svg>Evidence</div>
      <div class="cell"><div class="evidence" role="img" aria-label="Screenshot of the open file share listing"></div><div class="caption">Figure #1 – This is a caption for the above screenshot</div></div>
      <div class="side s3"><svg viewBox="0 0 10 10" fill="none" stroke="#fff" stroke-width="1.2"><rect x="2" y="1.5" width="6" height="8"/><path d="M4 4h2M4 6h2"/></svg>Recommendation</div>
      <div class="cell"><b>Restrict</b> share rights to named groups and move stored secrets into a managed vault.<ul><li>Rotate every credential found in the shares.</li><li>Audit folder permissions on a set schedule.</li></ul></div>
      <div class="side s4"><svg viewBox="0 0 10 10" fill="none" stroke="#fff" stroke-width="1.2"><rect x="1" y="1.5" width="8" height="5.5"/><path d="M5 7v2M3 9h4"/></svg>Assets Affected</div>
      <div class="cell"><ul><li>127.0.0.1</li><li>127.0.0.2</li><li>127.0.0.3</li></ul></div>
    </div>
  </div>
  <div class="page-foot">7</div>
</section>

<!-- Detailed: medium -->
<section class="page med" style="left:466px;top:610px">
  <div class="page-tab"></div>
  <div class="brand"><span class="brand-square"></span>ProbeWise</div>
  <div class="page-body">
    <h1>Detailed Observations</h1>
    <div class="finding-title"><div class="badge"><svg width="5" height="5" viewBox="0 0 5 5" fill="#fff"><rect x="0" y="3" width="1" height="2"/><rect x="2" y="2" width="1" height="3"/><rect x="4" y="0" width="1" height="5"/></svg></div><span>Medium Findings</span></div>
    <div class="finding">
      <div class="side hd">Insecure Configurations Identified</div><div class="cell hd">Critical</div>
      <div class="side s1"><svg viewBox="0 0 10 10" fill="none" stroke="#fff" stroke-width="1.4"><circle cx="4" cy="4" r="3"/><path d="M6.2 6.2 9 9"/></svg>Observation</div>
      <div class="cell">Several internal servers still accept outdated encryption protocols and weak cipher suites. An attacker on the same network segment could downgrade sessions and read traffic between users and these hosts.</div>
      <div class="side s2"><svg viewBox="0 0 10 10" fill="none" stroke="#fff" stroke-width="1.2"><rect x="1" y="3" width="8" height="6"/><path d="M3.5 3V1.5h3V3"/></svg>Evidence</div>
      <div class="cell"><div class="evidence" role="img" aria-label="Screenshot of the cipher scan results"></div><div class="caption">Figure #1 – This is a caption for the above screenshot</div></div>
      <div class="side s3"><svg viewBox="0 0 10 10" fill="none" stroke="#fff" stroke-width="1.2"><rect x="2" y="1.5" width="6" height="8"/><path d="M4 4h2M4 6h2"/></svg>Recommendation</div>
      <div class="cell"><b>Disable</b> legacy protocols and keep only current, strong cipher suites on all services.<ul><li>Apply one baseline across every server.</li><li>Rescan after changes to confirm the result.</li></ul></div>
      <div class="side s4"><svg viewBox="0 0 10 10" fill="none" stroke="#fff" stroke-width="1.2"><rect x="1" y="1.5" width="8" height="5.5"/><path d="M5 7v2M3 9h4"/></svg>Assets Affected</div>
      <div class="cell"><ul><li>127.0.0.1</li><li>127.0.0.2</li><li>127.0.0.3</li></ul></div>
    </div>
  </div>
  <div class="page-foot">8</div>
</section>

<!-- Detailed: low -->
<section class="page low" style="left:18px;top:908px">
  <div class="page-tab"></div>
  <div class="brand"><span class="brand-square"></span>ProbeWise</div>
  <div class="page-body">
    <h1>Detailed Observations</h1>
    <div class="finding-title"><div class="badge"><svg width="5" height="5" viewBox="0 0 5 5" fill="#fff"><rect x="0" y="3" width="1" height="2"/><rect x="2" y="2" width="1" height="3"/><rect x="4" y="0" width="1" height="5"/></svg></div><span>Low Findings</span></div>
    <div class="finding">
      <div class="side hd">Insecure Configurations Identified</div><div class="cell hd">Critical</div>
      <div class="side s1"><svg viewBox="0 0 10 10" fill="none" stroke="#fff" stroke-width="1.4"><circle cx="4" cy="4" r="3"/><path d="M6.2 6.2 9 9"/></svg>Observation</div>
      <div class="cell">Web responses omit a few recommended security headers and cookies lack some protective flags. On its own this adds little risk, but it weakens defences against script injection and framing attempts.</div>
      <div class="side s2"><svg viewBox="0 0 10 10" fill="none" stroke="#fff" stroke-width="1.2"><rect x="1" y="3" width="8" height="6"/><path d="M3.5 3V1.5h3V3"/></svg>Evidence</div>
      <div class="cell"><div class="evidence" role="img" aria-label="Screenshot of the response headers"></div><div class="caption">Figure #1 – This is a caption for the above screenshot</div></div>
      <div class="side s3"><svg viewBox="0 0 10 10" fill="none" stroke="#fff" stroke-width="1.2"><rect x="2" y="1.5" width="6" height="8"/><path d="M4 4h2M4 6h2"/></svg>Recommendation</div>
      <div class="cell"><b>Add</b> the standard security headers and set secure flags on all session cookies.<ul><li>Set headers once at the proxy layer.</li><li>Check new apps against this list before launch.</li></ul></div>
      <div class="side s4"><svg viewBox="0 0 10 10" fill="none" stroke="#fff" stroke-width="1.2"><rect x="1" y="1.5" width="8" height="5.5"/><path d="M5 7v2M3 9h4"/></svg>Assets Affected</div>
      <div class="cell"><ul><li>127.0.0.1</li><li>127.0.0.2</li><li>127.0.0.3</li></ul></div>
    </div>
  </div>
  <div class="page-foot">9</div>
</section>

<!-- Appendix -->
<section class="page" style="left:242px;top:908px">
  <div class="page-tab"></div>
  <div class="brand"><span class="brand-square"></span>ProbeWise</div>
  <div class="page-body">
    <h1 class="appendix-title">Appendix 01</h1>
    <h2 class="appendix-sub">Engagement Methodology</h2>
    <p>The team followed a staged approach: planning, discovery, scanning, manual testing, careful exploitation and reporting. Each stage was logged, and any action that could affect live service was agreed with the client in advance. Results were checked by a second tester before inclusion in this report.</p>
  </div>
  <div class="hex-field" role="img" aria-label="Faint hexagon pattern"></div>
  <div class="page-foot">10</div>
</section>

<!-- Contact -->
<section class="page" style="left:466px;top:908px">
  <div class="page-tab"></div>
  <div class="brand"><span class="brand-square"></span>ProbeWise</div>
  <div class="page-body">
    <h1>Our Contact</h1>
    <div class="contact-photo" role="img" aria-label="Black and white photo of a laptop on a desk beside a mug and notebook"></div>
    <ul class="contact-list">
      <li><span class="icon"><svg viewBox="0 0 10 10" fill="#fff"><path d="M5 0a3.5 3.5 0 0 0-3.5 3.5C1.5 6 5 10 5 10s3.5-4 3.5-6.5A3.5 3.5 0 0 0 5 0zm0 5a1.5 1.5 0 1 1 0-3 1.5 1.5 0 0 1 0 3z"/></svg></span><strong>Address</strong>567 Street Name, City, 12345</li>
      <li><span class="icon"><svg viewBox="0 0 10 10" fill="#fff"><path d="M2 0h2l1 3-1.5 1a6 6 0 0 0 2.5 2.5L7 5l3 1v2a2 2 0 0 1-2 2A8 8 0 0 1 0 2a2 2 0 0 1 2-2z"/></svg></span><strong>Phone</strong>123-456-789-01</li>
      <li><span class="icon"><svg viewBox="0 0 10 10" fill="none" stroke="#fff" stroke-width="1.2"><rect x="0.5" y="2" width="9" height="6"/><path d="M.5 2 5 5.5 9.5 2"/></svg></span><strong>Email</strong>contact@probewise.com</li>
      <li><span class="icon"><svg viewBox="0 0 10 10" fill="none" stroke="#fff" stroke-width="1.2"><rect x="0.5" y="1" width="9" height="6"/><path d="M5 7v2M3 9.3h4"/></svg></span><strong>Website</strong>www.probewise.com</li>
    </ul>
  </div>
  <div class="page-foot">11</div>
</section>

</body>
</html>
```